Menu Design Project

We trying to replace old flyer/menu with some new design.
hello this is my old menu i attached in email and my logo, the text you can pick from the menu and and i also attached some new picture for the food ,with my menu size unfold. front and back and then fold to 3.5" * 11". please show me what best can you do .Trifold is fine but must have image of food,
this is indian Restaurant
thats fine to have trifold menu design do to short time

Need to add also food picture on menu

Font styles to use
Serif
Decorative
Script

Colors

Designer to choose colors to be used in the design.

Requirements
Must have
• food image on menu
• trifold is fine ( do to short time)
• menu has to elegant ,color or text can be optional, Menu need to be neat and clean no too much rush on between the words .

```html
<!DOCTYPE html>
<html lang="en">
<head>
<meta charset="utf-8">
<title>Indian Restaurant Trifold Menu</title>
<link rel="stylesheet" href="https://fonts.googleapis.com/css2?family=Uncial+Antiqua&family=Barlow+Condensed:wght@300;400&display=swap">
<style>
:root{
  --maroon:#7c1015;
  --maroon-deep:#4e080b;
  --ink:#131011;
  --ink-soft:#1d1718;
  --card:#ffffff;
  --red:#b8262b;
  --red-bright:#d8343a;
  --text-dark:#2a2a2a;
  --text-light:#d6d2d0;
  --text-muted:#9a9594;
}
*{margin:0;padding:0;box-sizing:border-box}
html,body{width:1200px;height:943px;overflow:hidden;background:var(--ink)}
.menu{position:relative;width:1200px;height:943px;font-family:"Barlow Condensed",sans-serif}
.side-panel{position:absolute;top:0;width:300px;height:943px;background:radial-gradient(circle at 50% 40%,var(--maroon) 0%,var(--maroon-deep) 100%)}
.side-panel.left{left:0}
.side-panel.right{left:900px}
.center-panel{position:absolute;left:300px;top:0;width:600px;height:943px;background:linear-gradient(180deg,var(--ink-soft),var(--ink))}
.arch-card{position:absolute;top:0;left:0;width:300px;height:943px}
.section-title{position:absolute;font-family:"Uncial Antiqua",serif;font-weight:400;text-align:center;font-size:13px;line-height:17px;text-transform:lowercase;letter-spacing:.3px;white-space:nowrap}
.card-title{color:#111;width:180px;left:60px;top:64px}
.dark-title{color:#fff;width:300px}
.divider{position:absolute;height:1px;width:40px}
.card-divider{background:#333;left:130px;top:108px}
.dark-divider{background:#ddd}
.dish-list{position:absolute;list-style:none}
.dish-line{display:flex;align-items:baseline;white-space:nowrap}
.dish-name{text-transform:uppercase;font-weight:300}
.leader{flex:1;margin:0 4px;border-bottom:2px dotted var(--red);transform:translateY(-3px)}
.price{font-weight:300}
.dish-desc{font-size:5px;line-height:6px;margin:3px 0 0 14px;max-width:180px}
.on-card .dish{height:35.8px}
.on-card .dish-name,.on-card .price{color:var(--red);font-size:9.5px}
.on-card .dish-desc{color:var(--text-dark)}
.on-card{width:215px}
.on-dark .dish{height:28.6px}
.on-dark .dish-name{color:var(--text-light);font-size:9px}
.on-dark .price{color:var(--red-bright);font-size:9px}
.on-dark .dish-desc{color:var(--text-muted);max-width:200px}
.on-dark{width:213px}
.food-band{position:absolute;left:300px;top:412px;width:600px;height:146px;background:linear-gradient(100deg,#3a2a1e 0%,#8a8a86 25%,#b0782c 45%,#6b1c12 60%,#9a9a96 78%,#5a4a22 100%)}
</style>
</head>
<body>
<main class="menu">
  <section class="side-panel left">
    <svg class="arch-card" viewBox="0 0 300 943" aria-hidden="true"><path d="M18 914V130Q52 130 64 110C80 50 110 32 149 32C188 32 218 50 234 110Q246 130 280 130V914Z" fill="#fff"/></svg>
    <h2 class="section-title card-title">Non- vegetarian<br>appetizer</h2>
    <div class="divider card-divider"></div>
    <ul class="dish-list on-card" style="left:40px;top:126px">
      <li class="dish"><div class="dish-line"><span class="dish-name">Chicken Samosa</span><span class="leader"></span><span class="price">$5.99</span></div><p class="dish-desc">spicy chicken keema with peas wrapped in a light pastry</p></li>
      <li class="dish"><div class="dish-line"><span class="dish-name">Chicken Pakora</span><span class="leader"></span><span class="price">$10.99</span></div><p class="dish-desc">mildly spiced chicken fritters</p></li>
      <li class="dish"><div class="dish-line"><span class="dish-name">Fish Amritsari</span><span class="leader"></span><span class="price">$11.99</span></div><p class="dish-desc">mildly spiced boneless fish fritters</p></li>
      <li class="dish"><div class="dish-line"><span class="dish-name">Tawa Chicken</span><span class="leader"></span><span class="price">$12.99</span></div><p class="dish-desc">barbeque chicken sauteed with bell pepper and onion cooked in chef special</p></li>
      <li class="dish"><div class="dish-line"><span class="dish-name">Garlic Shrimp</span><span class="leader"></span><span class="price">$12.99</span></div><p class="dish-desc">shrimp cooked in white wine and chef special garlic sauce</p></li>
      <li class="dish"><div class="dish-line"><span class="dish-name">Spicy Wings</span><span class="leader"></span><span class="price">$0.00</span></div><p class="dish-desc">8 pcs of hot spicy buffalo wings all time favorite</p></li>
      <li class="dish"><div class="dish-line"><span class="dish-name">Tandoori Chicken</span><span class="leader"></span><span class="price">$7.99/$</span></div><p class="dish-desc">chicken marinated in yogurt and mild spices cooked in clay oven</p></li>
      <li class="dish"><div class="dish-line"><span class="dish-name">Lemon Chicken</span><span class="leader"></span><span class="price">$0.00</span></div><p class="dish-desc">chicken cooked with mild spices, lemon, and mango powder</p></li>
      <li class="dish"><div class="dish-line"><span class="dish-name">Chicken Seekh Kabab</span><span class="leader"></span><span class="price">$9.50</span></div><p class="dish-desc">ground chicken seasoned with fresh herbs and spices, rolled skewer</p></li>
      <li class="dish"><div class="dish-line"><span class="dish-name">Lamb Seekh Kabab</span><span class="leader"></span><span class="price">$11.99</span></div><p class="dish-desc">ground lamb seasoned with fresh herbs and spices, rolled skewer</p></li>
      <li class="dish"><div class="dish-line"><span class="dish-name">Chicken Tikka</span><span class="leader"></span><span class="price">$10.50</span></div><p class="dish-desc">boneless tender pieces of chicken seasoned with fresh herbs and yogurt cooked in clay oven</p></li>
      <li class="dish"><div class="dish-line"><span class="dish-name">Chicken Malai Kabab</span><span class="leader"></span><span class="price">$10.99</span></div><p class="dish-desc">boneless tender pieces of chicken marinated in sour cream</p></li>
      <li class="dish"><div class="dish-line"><span class="dish-name">Achari Tikka</span><span class="leader"></span><span class="price">$10.99</span></div><p class="dish-desc">boneless tender pieces of chicken marinated in pickle flavor sauce</p></li>
      <li class="dish"><div class="dish-line"><span class="dish-name">Afghani Chicken</span><span class="leader"></span><span class="price">$12.99</span></div><p class="dish-desc">mildly spiced chicken with savor cream cooked on a small fire</p></li>
      <li class="dish"><div class="dish-line"><span class="dish-name">Fish Tikka Tandoori</span><span class="leader"></span><span class="price">$11.99</span></div><p class="dish-desc">cubes of fish marinated in fresh herbs and ginger skewered in grill in tandoor</p></li>
      <li class="dish"><div class="dish-line"><span class="dish-name">Salmon Fish</span><span class="leader"></span><span class="price">$13.50</span></div><p class="dish-desc">cubes of salmon fish marinated in fresh herbs and ginger skewered and grilled in tandoor</p></li>
      <li class="dish"><div class="dish-line"><span class="dish-name">Tawa Fish</span><span class="leader"></span><span class="price">$12.99</span></div><p class="dish-desc">small piece of fish seasoned in yogurt and fresh herbs skewered and grilled in tandoor</p></li>
      <li class="dish"><div class="dish-line"><span class="dish-name">Tandoori Shrimp</span><span class="leader"></span><span class="price">$14.99</span></div><p class="dish-desc">6 pcs of jumbo shrimp marinated in yogurt, mild spices and herb</p></li>
      <li class="dish"><div class="dish-line"><span class="dish-name">Lamb Chop</span><span class="leader"></span><span class="price">$21.99</span></div><p class="dish-desc">5 pcs of rack of lamb marinated in traditional herbs and roasted in a clay oven on skewers</p></li>
      <li class="dish"><div class="dish-line"><span class="dish-name">Tandoori Mix Grill</span><span class="leader"></span><span class="price">$17.99</span></div><p class="dish-desc">a delicious combination of grilled chicken, seekh kabab and shrimp</p></li>
    </ul>
  </section>

  <section class="center-panel">
    <h2 class="section-title dark-title" style="left:0;top:26px">Vegetarian appetizer</h2>
    <div class="divider dark-divider" style="left:130px;top:57px"></div>
    <ul class="dish-list on-dark" style="left:40px;top:76px">
      <li class="dish"><div class="dish-line"><span class="dish-name">Vegetable Samosa</span><span class="leader"></span><span class="price">$2.99</span></div><p class="dish-desc">2pcs of spicy seasoned potatoes &amp; peas wrapped in light pastry</p></li>
      <li class="dish"><div class="dish-line"><span class="dish-name">Samosa Chaat</span><span class="leader"></span><span class="price">$7.49</span></div><p class="dish-desc">2pcs of samosa served with chutney &amp; chhole</p></li>
      <li class="dish"><div class="dish-line"><span class="dish-name">Aloo Tikki Chaat</span><span class="leader"></span><span class="price">$6.99</span></div><p class="dish-desc">4 pcs of aloo tikki served with chutney &amp; chhole</p></li>
      <li class="dish"><div class="dish-line"><span class="dish-name">Mix Veg. Pakora</span><span class="leader"></span><span class="price">$6.50</span></div><p class="dish-desc">Deep fried vegetable fritters dipped in chick peas flour</p></li>
      <li class="dish"><div class="dish-line"><span class="dish-name">Papri Chaat</span><span class="leader"></span><span class="price">$6.50</span></div><p class="dish-desc">mixture of crisp flour crackers served with potato, chick peas, mint/tamarind sauce &amp; yogurt</p></li>
      <li class="dish"><div class="dish-line"><span class="dish-name">Dahi Bhalla</span><span class="leader"></span><span class="price">$6.99</span></div><p class="dish-desc">softball of mixed lentils topped with yogurt, mint, &amp; tamarind sauce</p></li>
      <li class="dish"><div class="dish-line"><span class="dish-name">Paneer Pakora</span><span class="leader"></span><span class="price">$8.99</span></div><p class="dish-desc">7 pcs of deep fried cottage cheese fritters dipped in chick peas flour</p></li>
      <li class="dish"><div class="dish-line"><span class="dish-name">Vegetable Seekh Kabab</span><span class="leader"></span><span class="price">$8.99</span></div><p class="dish-desc">minced vegetable with cottage cheese seasoned with fresh herbs &amp; spices rolled skewers</p></li>
      <li class="dish"><div class="dish-line"><span class="dish-name">Paneer Tikka Tandoori</span><span class="leader"></span><span class="price">$11.99</span></div><p class="dish-desc">grilled paneer cheese, bell pepper, onion with a ginger flavor yogurt</p></li>
      <li class="dish"><div class="dish-line"><span class="dish-name">Chhole Bhature</span><span class="leader"></span><span class="price">$8.99</span></div><p class="dish-desc">2 pcs of large puffy shallow fried bread served with chick peas</p></li>
      <li class="dish"><div class="dish-line"><span class="dish-name">Stuffed Paneer Pakora</span><span class="leader"></span><span class="price">$8.50</span></div><p class="dish-desc">6 pcs of homemade cheese stuffed with mixture of delicious spiced potato &amp; mint</p></li>
      <li class="dish"><div class="dish-line"><span class="dish-name">Chatpati Aloo Chaat</span><span class="leader"></span><span class="price">$7.50</span></div></li>
    </ul>

    <h2 class="section-title dark-title" style="left:300px;top:26px">Indo-Chinese</h2>
    <div class="divider dark-divider" style="left:430px;top:57px"></div>
    <ul class="dish-list on-dark" style="left:340px;top:76px">
      <li class="dish"><div class="dish-line"><span class="dish-name">Chilli Paneer</span><span class="leader"></span><span class="price">$10.99</span></div><p class="dish-desc">cottage cheese sauteed with bell pepper &amp; onion in Indian Chinese spicy sauce</p></li>
      <li class="dish"><div class="dish-line"><span class="dish-name">Chilli Mushroom</span><span class="leader"></span><span class="price">$9.99</span></div><p class="dish-desc">mushroom sauteed with bell pepper &amp; onion in Indian Chinese spicy sauce</p></li>
      <li class="dish"><div class="dish-line"><span class="dish-name">Chilli Gobhi</span><span class="leader"></span><span class="price">$9.99</span></div><p class="dish-desc">gobhi sauteed with bell pepper &amp; onion in Indian Chinese spicy sauce</p></li>
      <li class="dish"><div class="dish-line"><span class="dish-name">Vegetable Manchurian</span><span class="leader"></span><span class="price">$10.50</span></div><p class="dish-desc">mix vegetable ball cooked in chef special garlic sauce</p></li>
      <li class="dish"><div class="dish-line"><span class="dish-name">Vegetable Chowmin</span><span class="leader"></span><span class="price">$8.30</span></div><p class="dish-desc">stir fry noodles &amp; thin sliced vegetables cooked in Chinese sauce</p></li>
      <li class="dish"><div class="dish-line"><span class="dish-name">Vegetable Spring Roll</span><span class="leader"></span><span class="price">$6.99</span></div><p class="dish-desc">carrots, red bell pepper, bean sprouts, and bamboo shoots wrapped in spring rolls</p></li>
      <li class="dish"><div class="dish-line"><span class="dish-name">Chilli Chicken</span><span class="leader"></span><span class="price">$10.99</span></div><p class="dish-desc">boneless chicken sauteed with bell pepper and onion cooked in spicy cheese sauce</p></li>
      <li class="dish"><div class="dish-line"><span class="dish-name">Chilli Fish</span><span class="leader"></span><span class="price">$13.99</span></div><p class="dish-desc">fish fritters sauteed with bell pepper and onion cooked in spices</p></li>
      <li class="dish"><div class="dish-line"><span class="dish-name">Chilli Shrimp</span><span class="leader"></span><span class="price">$12.99</span></div><p class="dish-desc">shrimp with bell pepper and onion cooked in spicy cheese sauce</p></li>
      <li class="dish"><div class="dish-line"><span class="dish-name">Chicken Manchurian</span><span class="leader"></span><span class="price">$10.99</span></div><p class="dish-desc">chicken ball cooked in a semi thick garlic flavor Chinese sauce</p></li>
      <li class="dish"><div class="dish-line"><span class="dish-name">Chicken Chowmin</span><span class="leader"></span><span class="price">$9.99</span></div><p class="dish-desc">stir fry noodles and thin sliced vegetables with chicken cooked in Chinese sauce</p></li>
    </ul>

    <h2 class="section-title dark-title" style="left:0;top:568px">Soup, salad, &amp; raita</h2>
    <div class="divider dark-divider" style="left:130px;top:599px"></div>
    <ul class="dish-list on-dark" style="left:40px;top:618px">
      <li class="dish"><div class="dish-line"><span class="dish-name">Tomato Soup</span><span class="leader"></span><span class="price">$3.99</span></div><p class="dish-desc">a simple soup made with fresh tomato</p></li>
      <li class="dish"><div class="dish-line"><span class="dish-name">Vegetarian Soup</span><span class="leader"></span><span class="price">$3.99</span></div><p class="dish-desc">a soup made with variety of vegetables</p></li>
      <li class="dish"><div class="dish-line"><span class="dish-name">Chicken Soup</span><span class="leader"></span><span class="price">$4.50</span></div><p class="dish-desc">the classic chicken soup consist of a clear broth, served with small pieces of chicken</p></li>
      <li class="dish"><div class="dish-line"><span class="dish-name">Hot N Sour Soup</span><span class="leader"></span><span class="price">$4.99</span></div><p class="dish-desc">a soup contains ingredients to make it both spicy and sour</p></li>
      <li class="dish"><div class="dish-line"><span class="dish-name">Fresh Garden Salad</span><span class="leader"></span><span class="price">$4.50</span></div></li>
      <li class="dish"><div class="dish-line"><span class="dish-name">Masala Salad</span><span class="leader"></span><span class="price">$5.99</span></div></li>
      <li class="dish"><div class="dish-line"><span class="dish-name">Mix Raita</span><span class="leader"></span><span class="price">$3.99</span></div></li>
      <li class="dish"><div class="dish-line"><span class="dish-name">Boondi Raita</span><span class="leader"></span><span class="price">$3.99</span></div></li>
      <li class="dish"><div class="dish-line"><span class="dish-name">Pudina Raita</span><span class="leader"></span><span class="price">$3.99</span></div></li>
      <li class="dish"><div class="dish-line"><span class="dish-name">Plain Dahi</span><span class="leader"></span><span class="price">$3.50</span></div></li>
    </ul>

    <h2 class="section-title dark-title" style="left:300px;top:568px">Seafood special</h2>
    <div class="divider dark-divider" style="left:430px;top:599px"></div>
    <ul class="dish-list on-dark" style="left:340px;top:618px">
      <li class="dish"><div class="dish-line"><span class="dish-name">Kadai Fish</span><span class="leader"></span><span class="price">$13.99</span></div><p class="dish-desc">boneless fish sauteed with bell pepper, onion, and fresh tomato</p></li>
      <li class="dish"><div class="dish-line"><span class="dish-name">Fish Curry</span><span class="leader"></span><span class="price">$13.99</span></div><p class="dish-desc">a delicious fish curry which is both rich and aromatic</p></li>
      <li class="dish"><div class="dish-line"><span class="dish-name">Fish Masala</span><span class="leader"></span><span class="price">$13.99</span></div><p class="dish-desc">ajwain flavor fish cooked with fresh garlic and tomato</p></li>
      <li class="dish"><div class="dish-line"><span class="dish-name">Goa Fish Curry</span><span class="leader"></span><span class="price">$12.59</span></div><p class="dish-desc">fish curry made in this style is tangy and spicy</p></li>
      <li class="dish"><div class="dish-line"><span class="dish-name">Fish Tikka Masala</span><span class="leader"></span><span class="price">$12.59</span></div><p class="dish-desc">chunks of roasted fish in a rich read creamy lightly spiced tomato based sauce</p></li>
      <li class="dish"><div class="dish-line"><span class="dish-name">Shrimp Curry</span><span class="leader"></span><span class="price">$12.99</span></div><p class="dish-desc">cooked with fresh ginger, onion, and tomato gravy</p></li>
      <li class="dish"><div class="dish-line"><span class="dish-name">Shrimp Masala</span><span class="leader"></span><span class="price">$12.99</span></div><p class="dish-desc">jumbo shrimp seasoned with chilli and lemon juice simmered in a sauce with exotic spices</p></li>
      <li class="dish"><div class="dish-line"><span class="dish-name">Shrimp Saag</span><span class="leader"></span><span class="price">$12.99</span></div><p class="dish-desc">shrimp cooked with fresh spinach</p></li>
      <li class="dish"><div class="dish-line"><span class="dish-name">Shrimp Bhuna</span><span class="leader"></span><span class="price">$12.99</span></div><p class="dish-desc">shrimp cooked with shredded onions, green peppers, and spices</p></li>
      <li class="dish"><div class="dish-line"><span class="dish-name">Shrimp Vindaloo</span><span class="leader"></span><span class="price">$12.99</span></div><p class="dish-desc">shrimp cooked with potato, vinegar, and lots of hot red chilli peppers</p></li>
      <li class="dish"><div class="dish-line"><span class="dish-name">Kadai Shrimp</span><span class="leader"></span><span class="price">$12.99</span></div><p class="dish-desc">shrimp sauteed with ginger, onion, fresh tomatoes, and oriental spices</p></li>
    </ul>
  </section>

  <div class="food-band" role="img" aria-label="Photograph of Indian curries and paneer dishes served in metal pans, seen from above"></div>

  <section class="side-panel right">
    <svg class="arch-card" viewBox="0 0 300 943" aria-hidden="true"><path d="M16 914V130Q50 130 62 110C78 50 108 32 149 32C190 32 220 50 236 110Q248 130 282 130V914Z" fill="#fff"/></svg>
    <h2 class="section-title card-title">Handi sen<br>(Non-veg)</h2>
    <div class="divider card-divider"></div>
    <ul class="dish-list on-card" style="left:40px;top:126px">
      <li class="dish"><div class="dish-line"><span class="dish-name">Chicken Makhni</span><span class="leader"></span><span class="price">$8.99</span></div><p class="dish-desc">chicken pieces roasted in a clay oven &amp; then folded into a spiced tomato creamy sauce</p></li>
      <li class="dish"><div class="dish-line"><span class="dish-name">Chicken Tikka Masala</span><span class="leader"></span><span class="price">$8.99</span></div><p class="dish-desc">chunks of roasted chicken sauteed with bell pepper, onion folded into a spiced tomato sauce</p></li>
      <li class="dish"><div class="dish-line"><span class="dish-name">Chicken Curry</span><span class="leader"></span><span class="price">$8.99</span></div><p class="dish-desc">all time favorite chicken, fresh ginger, onion and tomato gravy</p></li>
      <li class="dish"><div class="dish-line"><span class="dish-name">Chicken Korma</span><span class="leader"></span><span class="price">$8.99</span></div><p class="dish-desc">boneless chicken cooked in a rich cashew and onion sauce</p></li>
      <li class="dish"><div class="dish-line"><span class="dish-name">Kadai Chicken</span><span class="leader"></span><span class="price">$8.99</span></div><p class="dish-desc">marinated chicken sauteed with bellpepper, onion and fresh tomato</p></li>
      <li class="dish"><div class="dish-line"><span class="dish-name">Chicken Saag</span><span class="leader"></span><span class="price">$8.99</span></div><p class="dish-desc">chicked cooked with fresh spinach</p></li>
      <li class="dish"><div class="dish-line"><span class="dish-name">Chicken Jalfrezi</span><span class="leader"></span><span class="price">$8.99</span></div><p class="dish-desc">grilled cubes of chicken breast sauteed with fresh vegetables</p></li>
      <li class="dish"><div class="dish-line"><span class="dish-name">Chicken Masala</span><span class="leader"></span><span class="price">$8.99</span></div><p class="dish-desc">savory chicken seasoned with chilli and lemon juice simmered in a sauce with exotic spices</p></li>
      <li class="dish"><div class="dish-line"><span class="dish-name">Chicken Vindaloo</span><span class="leader"></span><span class="price">$8.99</span></div><p class="dish-desc">cubes of chicken cooked with onion and potato in a very hot sauce</p></li>
      <li class="dish"><div class="dish-line"><span class="dish-name">Goat Curry</span><span class="leader"></span><span class="price">$9.99</span></div><p class="dish-desc">traditional Mughlai offering - a special blnd of baby goat on bones and spices</p></li>
      <li class="dish"><div class="dish-line"><span class="dish-name">Goat Masala</span><span class="leader"></span><span class="price">$10.99</span></div><p class="dish-desc">baby goat seasoned with chilli and lemon juice simmered in a sauce with exotic spices</p></li>
      <li class="dish"><div class="dish-line"><span class="dish-name">Kadai Goat</span><span class="leader"></span><span class="price">$9.99</span></div><p class="dish-desc">goat sauteed with bell pepper, onion and fresh tomato</p></li>
      <li class="dish"><div class="dish-line"><span class="dish-name">Goat Saag</span><span class="leader"></span><span class="price">$9.99</span></div><p class="dish-desc">boneless tender pieces of goat cooked with fresh spinach sauce</p></li>
      <li class="dish"><div class="dish-line"><span class="dish-name">Goat Vindaloo</span><span class="leader"></span><span class="price">$9.99</span></div><p class="dish-desc">goat cooked with potato, vinegar and hot chilli</p></li>
      <li class="dish"><div class="dish-line"><span class="dish-name">Chicken Keema Mutter</span><span class="leader"></span><span class="price">$10.99</span></div><p class="dish-desc">cooked with potato, vinegar and lots of hot red chilli peppers</p></li>
      <li class="dish"><div class="dish-line"><span class="dish-name">Lamb Curry</span><span class="leader"></span><span class="price">$10.99</span></div><p class="dish-desc">a classic dish from Northern India and amongst the most popular of all curries</p></li>
      <li class="dish"><div class="dish-line"><span class="dish-name">Lamb Rogan Josh</span><span class="leader"></span><span class="price">$10.99</span></div><p class="dish-desc">boneless lamb cooked in Kashmir style</p></li>
      <li class="dish"><div class="dish-line"><span class="dish-name">Lamb Saag</span><span class="leader"></span><span class="price">$10.99</span></div><p class="dish-desc">lamb cooked with fresh spinach</p></li>
      <li class="dish"><div class="dish-line"><span class="dish-name">Lamb Korma</span><span class="leader"></span><span class="price">$10.99</span></div><p class="dish-desc">lamb cooked in light cream, almond and cashew nut sauce</p></li>
      <li class="dish"><div class="dish-line"><span class="dish-name">Lamb Bhuna Ghost</span><span class="leader"></span><span class="price">$10.99</span></div><p class="dish-desc">tender lamb cubes prepared with fresh ginger, onions, peppers, tomatoes and garlic</p></li>
      <li class="dish"><div class="dish-line"><span class="dish-name">Lamb Vindaloo</span><span class="leader"></span><span class="price">$10.99</span></div><p class="dish-desc">lamb cooked with potato, vinegar, and lots of hot red chilli peppers</p></li>
      <li class="dish"><div class="dish-line"><span class="dish-name">Lamb Keema Mutter</span><span class="leader"></span><span class="price">$12.99</span></div><p class="dish-desc">minced lamb cooked with peas, onions, tomatoes, herbs and spices</p></li>
    </ul>
  </section>
</main>
</body>
</html>
```